Looking for Classic Automotive Magazine Style Covers with emphasis on American Classic Cars, Car Brand, Automotive Products, Muscle Cars and Trucks.

The Final Graphics will be used for printing large scale Wall Art for Automotive Style Man Caves, used primarily to store and showcase Classic and American Muscle Cars.

4 individual Magazine Style covers are required, with titles such as Haul Rigs, Chrome Era, Drive Pulse and Rod Servicing etc.... .Final Media to be used for digital printing with final size at 1200mm wide by 3000mm high.

The type and style needed has been attached, but happy to consider any interesting idea provided.

Additionally 1xImage required for a final print size 3000mm x 3000mm.

```html
<!DOCTYPE html>
<html lang="en">
<head>
<meta charset="utf-8">
<title>Classic Automotive</title>
<link rel="stylesheet" href="https://fonts.googleapis.com/css2?family=Lato:ital,wght@0,700;0,900;1,900&family=Montserrat:wght@800&display=swap">
<style>
  :root {
    --backdrop: #d6d7c6;
    --poster-blue: #5c7db8;
    --poster-blue-deep: #53729f;
    --ink: #2a2228;
    --cream: #f6f1dc;
    --white: #ffffff;
    --yellow: #f7ef1f;
  }
  html, body {
    margin: 0;
    width: 1200px;
    height: 848px;
    overflow: hidden;
    background: var(--backdrop);
  }
  .poster {
    position: absolute;
    left: 210px;
    top: 34px;
    width: 780px;
    height: 780px;
    background: radial-gradient(circle at 50% 45%, var(--poster-blue) 0%, var(--poster-blue-deep) 100%);
    font-family: "Lato", sans-serif;
    overflow: hidden;
  }
  .poster p, .poster h1, .poster ul { margin: 0; }
  .rating {
    position: absolute;
    left: 316px;
    top: 37px;
    width: 160px;
    height: 26px;
  }
  .title {
    position: absolute;
    left: 0;
    right: 0;
    top: 58px;
    text-align: center;
    font-family: "Montserrat", sans-serif;
    font-weight: 800;
    font-size: 108px;
    line-height: 1;
    letter-spacing: 2px;
    color: var(--ink);
    padding-left: 14px;
    text-shadow:
      2px 0 0 var(--white), -2px 0 0 var(--white),
      0 2px 0 var(--white), 0 -2px 0 var(--white),
      1.5px 1.5px 0 var(--white), -1.5px 1.5px 0 var(--white),
      1.5px -1.5px 0 var(--white), -1.5px -1.5px 0 var(--white);
  }
  .speed-lines {
    position: absolute;
    top: 76px;
    width: 44px;
    height: 84px;
  }
  .speed-lines--left { left: 73px; }
  .speed-lines--right { left: 663px; }
  .ribbon {
    position: absolute;
    left: 190px;
    top: 180px;
    width: 406px;
    height: 56px;
  }
  .ribbon__label {
    position: absolute;
    left: 226px;
    top: 181px;
    width: 336px;
    height: 36px;
    line-height: 36px;
    text-align: center;
    font-weight: 900;
    font-style: italic;
    font-size: 25px;
    letter-spacing: 7px;
    color: var(--cream);
    white-space: nowrap;
  }
  .seal {
    position: absolute;
    left: 137px;
    top: 231px;
    width: 190px;
    height: 190px;
  }
  .seal__text {
    position: absolute;
    left: 137px;
    top: 231px;
    width: 190px;
    height: 190px;
    display: flex;
    flex-direction: column;
    align-items: center;
    justify-content: center;
    transform: rotate(-13deg);
    color: var(--ink);
    line-height: 1;
  }
  .seal__small {
    font-weight: 900;
    font-size: 20px;
    letter-spacing: 4px;
    margin-left: 4px;
  }
  .seal__big {
    font-weight: 900;
    font-size: 38px;
    margin-top: 2px;
  }
  .services {
    position: absolute;
    left: 416px;
    top: 255px;
    padding: 2px 0 2px 13px;
    list-style: none;
    border-left: 3px solid var(--cream);
    color: var(--cream);
    font-weight: 900;
    font-size: 21px;
    line-height: 23px;
    text-transform: uppercase;
    letter-spacing: -0.3px;
  }
  .car-art {
    position: absolute;
    left: 131px;
    top: 358px;
    width: 532px;
    height: 257px;
    border-radius: 48% 52% 50% 50% / 40% 40% 60% 60%;
    background: linear-gradient(180deg, var(--ink) 0%, #4a3f47 60%, var(--cream) 100%);
  }
  .tagline {
    position: absolute;
    left: 0;
    right: 0;
    top: 625px;
    text-align: center;
    font-weight: 900;
    font-size: 20px;
    letter-spacing: -0.6px;
    color: var(--ink);
  }
  .dealer {
    position: absolute;
    left: 0;
    right: 0;
    top: 657px;
    text-align: center;
    font-weight: 900;
    font-size: 39px;
    letter-spacing: 2px;
    color: var(--yellow);
    text-transform: uppercase;
  }
  .address {
    position: absolute;
    left: 0;
    right: 0;
    top: 703px;
    text-align: center;
    font-weight: 900;
    font-size: 21px;
    letter-spacing: -0.5px;
    color: #111018;
    text-transform: uppercase;
  }
  .website {
    position: absolute;
    left: 0;
    right: 0;
    top: 744px;
    text-align: center;
    font-weight: 700;
    font-size: 14px;
    color: var(--cream);
  }
</style>
</head>
<body>
  <main class="poster">
    <svg class="rating" viewBox="0 0 160 26" aria-hidden="true">
      <g fill="#2a2228">
        <polygon points="13,0 16.1,9.2 25.8,9.2 18,15 20.9,24.5 13,18.7 5.1,24.5 8,15 0.2,9.2 9.9,9.2"/>
        <polygon transform="translate(45 0)" points="13,0 16.1,9.2 25.8,9.2 18,15 20.9,24.5 13,18.7 5.1,24.5 8,15 0.2,9.2 9.9,9.2"/>
        <polygon transform="translate(90 0)" points="13,0 16.1,9.2 25.8,9.2 18,15 20.9,24.5 13,18.7 5.1,24.5 8,15 0.2,9.2 9.9,9.2"/>
        <polygon transform="translate(134 0)" points="13,0 16.1,9.2 25.8,9.2 18,15 20.9,24.5 13,18.7 5.1,24.5 8,15 0.2,9.2 9.9,9.2"/>
      </g>
    </svg>

    <svg class="speed-lines speed-lines--left" viewBox="0 0 44 84" aria-hidden="true">
      <g stroke="#f6f1dc" stroke-width="2.2">
        <line x1="0" y1="1" x2="44" y2="1"/><line x1="4" y1="9" x2="44" y2="9"/>
        <line x1="2" y1="17" x2="44" y2="17"/><line x1="6" y1="25" x2="44" y2="25"/>
        <line x1="3" y1="33" x2="44" y2="33"/><line x1="6" y1="42" x2="44" y2="42"/>
        <line x1="3" y1="51" x2="44" y2="51"/><line x1="6" y1="59" x2="44" y2="59"/>
        <line x1="2" y1="67" x2="44" y2="67"/><line x1="4" y1="75" x2="44" y2="75"/>
        <line x1="0" y1="83" x2="44" y2="83"/>
      </g>
    </svg>
    <svg class="speed-lines speed-lines--right" viewBox="0 0 44 84" aria-hidden="true">
      <g stroke="#f6f1dc" stroke-width="2.2">
        <line x1="0" y1="1" x2="44" y2="1"/><line x1="0" y1="9" x2="40" y2="9"/>
        <line x1="0" y1="17" x2="42" y2="17"/><line x1="0" y1="25" x2="38" y2="25"/>
        <line x1="0" y1="33" x2="41" y2="33"/><line x1="0" y1="42" x2="38" y2="42"/>
        <line x1="0" y1="51" x2="41" y2="51"/><line x1="0" y1="59" x2="38" y2="59"/>
        <line x1="0" y1="67" x2="42" y2="67"/><line x1="0" y1="75" x2="40" y2="75"/>
        <line x1="0" y1="83" x2="44" y2="83"/>
      </g>
    </svg>

    <h1 class="title">CLASSIC</h1>

    <svg class="ribbon" viewBox="0 0 406 56" aria-hidden="true">
      <polygon fill="#2a2228" points="22,18 2,52 34,52 36,18"/>
      <polygon fill="#2a2228" points="384,18 404,52 372,52 370,18"/>
      <rect x="36" y="1" width="334" height="36" fill="#2a2228"/>
    </svg>
    <p class="ribbon__label">• AUTOMOTIVE •</p>

    <svg class="seal" viewBox="0 0 190 190" aria-hidden="true">
      <circle cx="95" cy="95" r="84" fill="#ffffff"/>
      <circle cx="95" cy="95" r="88" fill="none" stroke="#ffffff" stroke-width="10" stroke-dasharray="3 3"/>
    </svg>
    <div class="seal__text">
      <span class="seal__small">HOT ROD &amp;</span>
      <span class="seal__big">CUSTOM</span>
    </div>

    <ul class="services">
      <li>Haul Rigs</li>
      <li>Chrome Era</li>
      <li>Drive Pulse</li>
      <li>Rod Servicing</li>
    </ul>

    <div class="car-art" role="img" aria-label="Engraved-style illustration of a 1930s classic sedan standing on a cream oval spotlight"></div>

    <p class="tagline">YOUR FRIENDLY NEIGHBOURHOOD DEALERSHIP</p>
    <p class="dealer">Copperline Motor Co.</p>
    <p class="address">Mesa Ridge Avenue 35 Street, Arizona</p>
    <p class="website">www.copperlinemotor.com</p>
  </main>
</body>
</html>
```